Business Card desgin, company called Tall Orbit.

I am looking for the logo colors (3) to be used on the card in whatever design you think might work. the certifications are on the back (4) on the front will be my name, Dana Whitlock, owner/instructor, phone 317.582.4096, website www.tlo-coaching.example, email dw@tlo-coaching.example. im flexible on fonts.

Target Market(s)

firearms owners

Industry/Entity Type

firearms training

Contact Information for Business Card

certification icons on back

```html
<!DOCTYPE html>
<html lang="en">
<head>
<meta charset="utf-8">
<title>Tall Orbit – Business Card</title>
<link rel="stylesheet" href="https://fonts.googleapis.com/css2?family=Montserrat:wght@400;600;700&family=Playfair+Display:wght@500&display=swap">
<style>
  :root {
    --stage: #1c1d20;
    --navy: #0c2541;
    --navy-soft: #183453;
    --red: #c9202f;
    --white: #ffffff;
    --rule: #8a97a8;
    --badge-orange: #f08a1c;
    --badge-dark: #1a1c22;
    --badge-gold: #d99a2b;
    --badge-blue: #2f6fb3;
  }
  * { margin: 0; padding: 0; box-sizing: border-box; }
  html, body { width: 1200px; height: 874px; overflow: hidden; background: var(--stage); }
  .canvas { position: relative; width: 1200px; height: 874px; }

  .card {
    position: absolute;
    left: 290px;
    width: 620px;
    height: 354px;
    border-radius: 20px;
    background: var(--navy);
    overflow: hidden;
    font-family: "Montserrat", sans-serif;
  }
  .card--back { top: 48px; }
  .card--front { top: 462px; }

  /* Back: brand + certifications */
  .brand-block { position: absolute; left: 104px; top: 92px; display: flex; align-items: center; gap: 26px; }
  .brand-dot { width: 74px; height: 74px; border-radius: 50%; border: 7px solid var(--white); flex: none; }
  .brand-name { color: var(--red); font-weight: 700; font-size: 40px; letter-spacing: 2px; text-transform: uppercase; line-height: 1; }
  .brand-url { font-family: "Playfair Display", serif; font-weight: 500; color: var(--white); font-size: 19px; letter-spacing: .5px; margin-top: 8px; }

  .cert-row { position: absolute; left: 50px; right: 50px; top: 236px; display: flex; justify-content: space-between; align-items: flex-end; }
  .cert { width: 62px; height: 62px; }

  /* Front: contact */
  .watermark { position: absolute; left: -70px; top: -60px; width: 380px; height: 380px; border-radius: 50%; border: 34px solid var(--navy-soft); }
  .person { position: absolute; left: 46px; top: 122px; }
  .person-name { color: var(--red); font-weight: 700; font-size: 27px; }
  .person-role { color: var(--white); font-size: 14px; margin-top: 4px; }
  .divider { position: absolute; left: 46px; right: 46px; top: 196px; height: 1px; background: var(--rule); }
  .contact-list { position: absolute; left: 46px; top: 212px; list-style: none; }
  .contact-item { display: flex; align-items: center; gap: 12px; color: var(--white); font-size: 15px; line-height: 26px; }
  .contact-icon { width: 14px; height: 14px; fill: var(--red); flex: none; }

  .front-brand { position: absolute; right: 50px; top: 70px; display: flex; flex-direction: column; align-items: center; gap: 16px; }
  .front-brand .brand-name { font-size: 22px; letter-spacing: 1.5px; }
  .front-brand .brand-dot { width: 140px; height: 140px; border-width: 12px; }
</style>
</head>
<body>
<main class="canvas">

  <section class="card card--back" aria-label="Card back with certifications">
    <div class="brand-block">
      <span class="brand-dot" aria-hidden="true"></span>
      <div>
        <div class="brand-name">Tall Orbit</div>
        <div class="brand-url">WWW.TLO-Coaching.example</div>
      </div>
    </div>
    <div class="cert-row">
      <svg class="cert" viewBox="0 0 62 62" role="img" aria-label="Tactical instructor certification badge">
        <path d="M31 4 L56 12 V32 C56 46 44 55 31 59 C18 55 6 46 6 32 V12 Z" fill="var(--badge-orange)"/>
        <path d="M31 10 L50 16 V30 C50 40 41 47 31 51 C21 47 12 40 12 30 V16 Z" fill="var(--white)"/>
      </svg>
      <svg class="cert" viewBox="0 0 62 62" role="img" aria-label="Firearms instructor certification badge">
        <rect x="8" y="6" width="46" height="50" rx="6" fill="var(--badge-dark)"/>
        <rect x="4" y="40" width="54" height="10" rx="3" fill="var(--badge-blue)"/>
      </svg>
      <svg class="cert" viewBox="0 0 62 62" role="img" aria-label="Range safety officer certification badge">
        <rect x="8" y="6" width="46" height="50" rx="6" fill="var(--badge-dark)"/>
        <rect x="4" y="30" width="54" height="10" rx="3" fill="var(--badge-gold)"/>
      </svg>
      <svg class="cert" viewBox="0 0 62 62" role="img" aria-label="Concealed carry instructor certification badge">
        <rect x="4" y="4" width="54" height="54" fill="var(--white)"/>
        <path d="M31 12 L48 18 V32 C48 42 40 48 31 51 C22 48 14 42 14 32 V18 Z" fill="var(--red)"/>
      </svg>
    </div>
  </section>

  <section class="card card--front" aria-label="Card front with contact details">
    <span class="watermark" aria-hidden="true"></span>
    <div class="person">
      <div class="person-name">Dana Whitlock</div>
      <div class="person-role">owner/instructor</div>
    </div>
    <div class="divider"></div>
    <ul class="contact-list">
      <li class="contact-item">
        <svg class="contact-icon" viewBox="0 0 24 24" aria-hidden="true"><path d="M6.6 10.8a15.1 15.1 0 0 0 6.6 6.6l2.2-2.2a1 1 0 0 1 1-.25 11.4 11.4 0 0 0 3.6.57 1 1 0 0 1 1 1V20a1 1 0 0 1-1 1A17 17 0 0 1 3 4a1 1 0 0 1 1-1h3.5a1 1 0 0 1 1 1c0 1.25.2 2.45.57 3.57a1 1 0 0 1-.25 1z"/></svg>
        317.582.4096
      </li>
      <li class="contact-item">
        <svg class="contact-icon" viewBox="0 0 24 24" aria-hidden="true"><path d="M2 5h20v14H2z M3 6l9 7 9-7" fill="var(--red)"/><path d="M3 6l9 7 9-7" fill="none" stroke="var(--navy)" stroke-width="2"/></svg>
        dw@tlo-coaching.example
      </li>
      <li class="contact-item">
        <svg class="contact-icon" viewBox="0 0 24 24" aria-hidden="true"><circle cx="12" cy="12" r="10"/><path d="M2 12h20M12 2c3 3 3 17 0 20M12 2c-3 3-3 17 0 20" fill="none" stroke="var(--navy)" stroke-width="1.6"/></svg>
        www.tlo-coaching.example
      </li>
    </ul>
    <div class="front-brand">
      <div class="brand-name">Tall Orbit</div>
      <span class="brand-dot" aria-hidden="true"></span>
    </div>
  </section>

</main>
</body>
</html>
```